依頼詳細
◇必須項目
・パララックス実装
・各メニューのアイコンなどでわかりやすくしてほしい
・英語の表記は出来る限り減らして欲しい
・今後観光のサイトを作成の予定があるのでバナーで飛べるようにしてほしい。
・現行の黒いサイトへのリンクも必要。

◇参考サイト
ミルヴェスタ  http://www.web-morvesta.net/ デザイン性があってブランド感が好き
ソビエント http://tovira.kumogi.ne.jp/client-check/sobient/index.html ロゴなどがああって分かりやすいから好き。

◇現行サイト
リニューアル予定サイトhttp://www.rensho-kyoto.co.jp/
サテライトサイトhttp://www.rensho-kyoto.com/

◇サイトマップ
①Home
② 8つのこだわり
③結婚指輪
④ 婚約指輪
⑤セット指輪
⑥ アクセサリー
⑦ デザイナー紹介
⑧店舗紹介
⑨お問い合わせ
⑩BLOG(一覧)
⑪BLOG(詳細)
⑫NEWS(一覧)
⑬NEWS(詳細)
⑭ご来店の前に
⑮結婚までの流れ
⑯お客様の声(一覧)
⑰お客様の声(詳細)
⑱HOW TO (ジュエリーの知識など)

◇優先事項
1.凝ったデザイン
2.ユーザビリティー
3.編集更新 ※詳しいので難しくても大丈夫

◇期待する効果
1.ブランディング
2.認知度の向上
3.SEO対策

◇ターゲット
【性別】女性
【年代】20代後半~40代
【属性】会社員 自営業

◇sns
Instagram 会社用 後々やる予定
Facebook 会社用
Twitter 会社用

その他
予約システム
サイトURL
http://www.rensho-kyoto.co.jp/
ページ数
1ページ
希望イメージ
シンプル 複雑
単色 カラフル
暗い 明るい
日常 高級
遊び心 厳粛
未来的 伝統的
女性的 男性的
希望する色
カラーは基本的にお任せします。紫や濃い青色は縁起的に控えて下さい。
納品ファイル
• イラストレーター形式 (.ai)
• フォトショップ形式 (.psd)
• PNG形式 (.png)
補足説明
素材①
店内写真などをブリムコンテナを使って、アップしています。
下記URLよりダウンロードしてください。
■ダウンロードURL:
http://brimcontena.jp/download/9a1c3e7b2d4f6a8c0e1b3d5f7a9c2e4b6d8f0a1c
http://brimcontena.jp/download/7e2b4d6f8a0c1e3b5d7f9a2c4e6b8d0f1a3c5e7b

ダウンロードパスワード pass

素材②
ピクセノ:https://jp.pixeno-stock.com/
当社で定期契約をしています。クレジット購入のみのもの以外をご利用下さい。
また定期契約のものは弊社の負担となり、ランサー様に負担はありません。
カンプ画像を入れてください。

素材③
現行サイトより引用してください。
URL:http://www.rensho-kyoto.co.jp/
画像やテキストに関しては一旦引き抜いて頂いて構いません。

提案がないため、延長をさせて頂きます。
宜しくお願いたします!
もう少し提案が見たいため、延長を行わせて頂きます!
宜しくお願い致します!
提案が少ない為、延長させて頂きます。
テイストが少し違う部分もありますので詳細に関しては、別途報告させて頂きます。
宜しくお願い致します!
お世話になります。
テイストの伝え方が決定しましたのでお伝えします。

サイト全体の色味に関してですが、参考サイトをとして上げている、グレーやベージュなどを上手く使って和の雰囲気を出してほしいです。※全体的に緑を全面に打ち出したカラーが多いので少し変えてほしいです。
和に関しては、鳳林寺より雪峯寺、平安より室町、舞妓より芸子のイメージを考えています。パッと艶やかな京都ではなく京都の落ち着いた部分をメインに打ち出して頂きたいです。
また、和の雰囲気の出し方ですが画像に頼ったものはやめていただきたいです。
例えば、画像部分をグレーのダミー画像を使ったとしても和を感じれる様にデザインをお願いします。
全体的に画像に頼ったデザインが多いので画像を切ってはっただけのようなデザインは控えていただくようにお願いします。
ただ、和柄を使うだけではなく日本特有の間のとり方を使って平坦なデザインにならない様にお願いします。(和柄を使ってはだめなわけではありません。)
HPを見た人すべてが良いと感じるデザインでなくても問題ありませんがブランドのイメージをHP上で打ち出す表現は必須です。
何処かで見たことのあるデザインだけではなく、あまり見たことのないサイトデザインを希望しています。
自分自身デザイナーなのでデザインの意図や意味を大事にしています。
WEB上での動的な動きを含めて、和のテイストをより感じれるようなデザインが理想的です。
出来る限りデザインの意味や動的要因の説明を含めて提案を頂ければ幸いです。

ひと目見て気に入りました。

とてもデザイン性が高く満足しております。

```html
<!DOCTYPE html>
<html lang="ja">
<head>
<meta charset="utf-8">
<title>蓮匠 | 京都の結婚指輪・婚約指輪</title>
<link rel="stylesheet" href="https://fonts.googleapis.com/css2?family=Shippori+Mincho:wght@400;500&display=swap">
<style>
:root{
  --paper:#ffffff;
  --ink:#3b3733;
  --ink-soft:#6d6760;
  --rule:#4a4541;
  --beige:#f1e3c2;
  --beige-pale:#f8f1e2;
  --hero-dark:#2c2621;
  --hero-warm:#6a5440;
  --ring-green:#5c6a1c;
  --ring-brown:#4a3424;
}
*{margin:0;padding:0;box-sizing:border-box}
html,body{width:1200px;height:4372px;overflow:hidden;background:var(--paper)}
body{position:relative;font-family:"Shippori Mincho",serif;color:var(--ink)}
.abs{position:absolute}
.vert{writing-mode:vertical-rl;text-orientation:upright}
ul{list-style:none}
a{color:inherit;text-decoration:none}

/* hero */
.hero{left:0;top:0;width:1200px;height:500px;
  background:linear-gradient(160deg,var(--hero-dark) 0%,var(--hero-warm) 45%,#3a3128 75%,#1f1b18 100%)}
.hero-curve{left:0;top:0;width:1200px;height:520px}
.brand-panel{left:160px;top:0;width:164px;height:600px;background:var(--paper);
  box-shadow:0 2px 10px rgba(0,0,0,.12);border:1px solid #e6ddd0}
.brand-mark{left:56px;top:40px;width:52px;height:52px;border:2px solid var(--ink);border-radius:50%}
.brand-name{left:0;top:104px;width:164px;text-align:center;font-size:13px;letter-spacing:.3em}
.brand-copy{left:48px;top:170px;height:290px;font-size:15px;line-height:32px;letter-spacing:.12em}
.sns{left:40px;top:500px;display:flex;gap:16px}
.sns span{display:block;width:20px;height:20px;background:var(--ink)}
.reserve-tab{left:1130px;top:70px;width:42px;height:170px;background:var(--paper);
  border:1px solid #d9d0c3;font-size:14px;letter-spacing:.2em;display:flex;align-items:center;justify-content:center}

/* navigation */
.global-nav{left:360px;top:540px;width:780px}
.global-nav ul{display:flex;flex-direction:row-reverse;justify-content:space-between;align-items:flex-start}
.global-nav li{writing-mode:vertical-rl;text-orientation:upright;font-size:14px;letter-spacing:.18em}

/* shared */
.title{font-size:46px;font-weight:400;letter-spacing:.2em;line-height:1}
.accent-block{background:var(--beige)}
.pale-block{background:var(--beige-pale)}
.more{width:48px;height:160px;border:1px solid var(--ink-soft);background:var(--paper);
  font-size:13px;letter-spacing:.3em;display:flex;align-items:center;justify-content:center}
.photo{display:block}
.ornament-line{fill:none;stroke:var(--rule);stroke-width:2}

/* 8 commitments */
.commit-list{left:540px;top:820px;width:470px}
.commit-list ul{display:flex;flex-direction:row-reverse;justify-content:space-between;align-items:flex-start}
.commit-list li{writing-mode:vertical-rl;text-orientation:upright;font-size:13px;letter-spacing:.12em}
.commit-photo{left:80px;top:800px;width:400px;height:360px;
  background:linear-gradient(180deg,#d6cbbd 0%,#c4ab8e 55%,#8c6a4f 100%)}

/* collection */
.collection-grid{left:388px;top:1500px;display:grid;grid-template-columns:repeat(3,208px);
  grid-auto-rows:200px;column-gap:32px;row-gap:12px}
.collection-grid .photo{background:linear-gradient(180deg,#6f7d24 0%,var(--ring-green) 62%,var(--ring-brown) 66%,#2f2118 100%)}

/* designers */
.designer{top:2460px;width:220px;height:580px;background:linear-gradient(180deg,#8d8d8d 0%,#4e4e4e 60%,#2b2b2b 100%)}

/* blog */
.blog-list{left:300px;top:3520px;width:500px}
.blog-list li{height:44px;border-bottom:1px solid #c9c0b3;display:flex;align-items:flex-end;
  padding-bottom:8px;font-size:12px;letter-spacing:.05em;gap:22px;color:var(--ink-soft)}
.blog-list time{color:var(--ink)}

/* footer */
.footer-mark{left:570px;top:4020px;width:60px;height:60px;border:2px solid var(--ink);border-radius:50%}
.footer-name{left:0;top:4094px;width:1200px;text-align:center;font-size:14px;letter-spacing:.3em}
.address{left:0;top:4172px;width:1200px;text-align:center;font-size:12px;letter-spacing:.08em;color:var(--ink-soft)}
.copyright{left:0;top:4306px;width:1200px;text-align:center;font-size:10px;letter-spacing:.06em;color:var(--ink-soft)}
</style>
</head>
<body>

<!-- header -->
<div class="abs hero photo" role="img" aria-label="京都の町家が並ぶ夕暮れの路地と店舗の入り口"></div>
<svg class="abs hero-curve" width="1200" height="520" viewBox="0 0 1200 520" aria-hidden="true">
  <path d="M0 400 Q600 500 1200 380 L1200 520 L0 520Z" fill="#ffffff"/>
</svg>

<header class="abs brand-panel">
  <div class="abs brand-mark"></div>
  <p class="abs brand-name">蓮匠</p>
  <p class="abs brand-copy vert">京都の職人技術を<br>結婚指輪と婚約指輪の専門店</p>
  <div class="abs sns" aria-label="SNSリンク">
    <span role="img" aria-label="フェイスブック"></span>
    <span role="img" aria-label="インスタグラム"></span>
    <span role="img" aria-label="ツイッター"></span>
  </div>
</header>

<a class="abs reserve-tab vert">ご来店予約</a>

<nav class="abs global-nav">
  <ul>
    <li>８つのこだわり</li>
    <li>コレクション</li>
    <li>デザイナー紹介</li>
    <li>ブログ</li>
    <li>店舗紹介</li>
    <li>ご来店の前に</li>
    <li>結婚までの流れ</li>
    <li>お客様の声</li>
    <li>お問い合わせ</li>
  </ul>
</nav>

<!-- 8 commitments -->
<svg class="abs" style="left:480px;top:640px" width="720" height="80" viewBox="0 0 720 80" aria-hidden="true">
  <path class="ornament-line" d="M0 20 H90"/>
  <path class="ornament-line" d="M60 30 H660 Q700 30 700 70"/>
</svg>
<div class="abs accent-block" style="left:1040px;top:700px;width:76px;height:240px"></div>
<h2 class="abs title vert" style="left:1000px;top:730px">８つのこだわり</h2>

<div class="abs commit-list">
  <ul>
    <li>一、「手仕事」の美学</li>
    <li>二、「京都」を身近に</li>
    <li>三、デザインへの想い</li>
    <li>四、一生ものの品質を</li>
    <li>五、素材の選定</li>
    <li>六、一点物のお誂え</li>
    <li>七、アフター保証</li>
    <li>八、ご来店のお約束</li>
  </ul>
</div>

<div class="abs commit-photo photo" role="img" aria-label="木箱に収められた結婚指輪"></div>
<svg class="abs" style="left:0;top:1190px" width="480" height="20" aria-hidden="true">
  <path class="ornament-line" d="M0 10 H470"/>
</svg>
<a class="abs more vert" style="left:470px;top:1120px">詳しく見る</a>

<!-- collection -->
<svg class="abs" style="left:0;top:1360px" width="420" height="70" viewBox="0 0 420 70" aria-hidden="true">
  <path class="ornament-line" d="M0 10 H360 Q400 10 400 50"/>
</svg>
<div class="abs accent-block" style="left:160px;top:1400px;width:120px;height:180px"></div>
<h2 class="abs title vert" style="left:186px;top:1420px">コレクション</h2>
<div class="abs pale-block" style="left:560px;top:1840px;width:580px;height:400px"></div>
<div class="abs collection-grid">
  <div class="photo" role="img" aria-label="ダイヤモンドの婚約指輪"></div>
  <div class="photo" role="img" aria-label="ダイヤモンドの婚約指輪"></div>
  <div class="photo" role="img" aria-label="ダイヤモンドの婚約指輪"></div>
  <div class="photo" role="img" aria-label="ダイヤモンドの婚約指輪"></div>
  <div class="photo" role="img" aria-label="ダイヤモンドの婚約指輪"></div>
  <div class="photo" role="img" aria-label="ダイヤモンドの婚約指輪"></div>
  <div class="photo" role="img" aria-label="ダイヤモンドの婚約指輪"></div>
  <div class="photo" role="img" aria-label="ダイヤモンドの婚約指輪"></div>
  <div class="photo" role="img" aria-label="ダイヤモンドの婚約指輪"></div>
</div>
<a class="abs more vert" style="left:240px;top:2020px">詳しく見る</a>

<!-- designers -->
<svg class="abs" style="left:0;top:2390px" width="460" height="70" viewBox="0 0 460 70" aria-hidden="true">
  <path class="ornament-line" d="M0 10 H400 Q440 10 440 50"/>
</svg>
<div class="abs accent-block" style="left:1020px;top:2360px;width:120px;height:200px"></div>
<h2 class="abs title vert" style="left:980px;top:2370px">デザイナー紹介</h2>
<div class="abs pale-block" style="left:40px;top:2760px;width:760px;height:440px"></div>
<div class="abs designer photo" style="left:80px" role="img" aria-label="デザイナーのモノクロ肖像写真"></div>
<div class="abs designer photo" style="left:320px" role="img" aria-label="デザイナーのモノクロ肖像写真"></div>
<div class="abs designer photo" style="left:560px" role="img" aria-label="デザイナーのモノクロ肖像写真"></div>
<a class="abs more vert" style="left:920px;top:2880px">詳しく見る</a>

<!-- blog -->
<div class="abs pale-block" style="left:800px;top:3280px;width:240px;height:320px"></div>
<div class="abs accent-block" style="left:160px;top:3360px;width:120px;height:160px"></div>
<h2 class="abs title vert" style="left:186px;top:3370px">ブログ</h2>
<div class="abs blog-list">
  <ul>
    <li><time>2015.10.22</time>京都と出張相談会のご案内と結婚指輪フェアのお知らせ</li>
    <li><time>2015.10.22</time>京都と出張相談会のご案内と結婚指輪フェアのお知らせ</li>
    <li><time>2015.10.22</time>京都と出張相談会のご案内と結婚指輪フェアのお知らせ</li>
    <li><time>2015.10.22</time>京都と出張相談会のご案内と結婚指輪フェアのお知らせ</li>
    <li><time>2015.10.22</time>京都と出張相談会のご案内と結婚指輪フェアのお知らせ</li>
    <li><time>2015.10.22</time>京都と出張相談会のご案内と結婚指輪フェアのお知らせ</li>
  </ul>
</div>
<a class="abs more vert" style="left:840px;top:3600px">詳しく見る</a>
<svg class="abs" style="left:720px;top:3840px" width="480" height="70" viewBox="0 0 480 70" aria-hidden="true">
  <path class="ornament-line" d="M20 60 Q20 30 60 30 H480"/>
</svg>

<!-- footer -->
<footer>
  <div class="abs footer-mark"></div>
  <p class="abs footer-name">蓮匠</p>
  <p class="abs address">〒604-0000　京都府京都市中京区蓮町123番地　蓮匠本店</p>
  <p class="abs copyright">© 2015 蓮匠 京都の結婚指輪・婚約指輪専門店 All Rights Reserved.</p>
</footer>

</body>
</html>
```